Clear Harbor Transportation Management Association

We are looking to design an awards certificate for an upcoming event that we are having in December. This award would be given to our employee members who have done an outstanding job of promoting commuting alternatives (biking, walking, transit, ridesharing) to driving alone, and as such have reduced green house gas emissions. We are looking for a cool graphic that will make the award something special and worth framing. Attached is our current logo which should be on the certificate somewhere, as well as a few of our program design logos which can be used for inspiration.

Target Market(s)

Board members

Industry/Entity Type

Event

Requirements
Must have
• Graphic suitable for framing as part of an awards certificate
Nice to have
• Something that relates to what we do which is promoting sustainable tranportation (biking, walking, transit, and ridesharing).

```html
<!DOCTYPE html>
<html lang="en">
<head>
<meta charset="utf-8">
<title>Certificate of Appreciation – Clear Harbor TMA</title>
<link rel="stylesheet" href="https://fonts.googleapis.com/css2?family=Montserrat:wght@700;800&family=Cabin:wght@400&family=Arimo:wght@400&family=Parisienne&family=Lato:wght@400;700&display=swap">
<style>
  :root {
    --sky-top: #4fa9dc;
    --sky-mid: #5dbde6;
    --sky-low: #7fd0ea;
    --ink: #1d2126;
    --ink-soft: #4a5560;
    --ribbon: #f01d1d;
    --ribbon-dark: #c81414;
    --white: #ffffff;
    --gold: #c99a2e;
    --gold-light: #e4c25e;
    --sketch: rgba(80, 130, 160, 0.35);
  }
  html, body {
    margin: 0;
    padding: 0;
    overflow: hidden;
    background: #ffffff;
  }
  .certificate {
    position: relative;
    width: 946px;
    height: 1200px;
    overflow: hidden;
    background: linear-gradient(180deg, var(--sky-top) 0%, var(--sky-mid) 45%, var(--sky-low) 100%);
    font-family: "Lato", sans-serif;
    color: var(--ink);
  }
  .sky-backdrop {
    position: absolute;
    inset: 0;
    background:
      radial-gradient(ellipse 60% 30% at 45% 12%, rgba(150, 225, 240, 0.55), transparent 70%),
      radial-gradient(ellipse 90% 35% at 50% 80%, rgba(220, 245, 252, 0.45), transparent 70%);
  }
  .org-name {
    position: absolute;
    top: 62px;
    left: 0;
    right: 0;
    text-align: center;
    font-family: "Montserrat", sans-serif;
    font-weight: 700;
    font-size: 20px;
    line-height: 27px;
    letter-spacing: 0.5px;
    color: #2b3038;
    margin: 0;
  }
  .stars {
    position: absolute;
    top: 138px;
    left: 0;
    right: 0;
    text-align: center;
    color: var(--white);
    font-size: 18px;
    letter-spacing: 6px;
  }
  .title {
    position: absolute;
    top: 168px;
    left: 0;
    right: 0;
    text-align: center;
    margin: 0;
    font-family: "Montserrat", sans-serif;
    font-weight: 800;
    font-size: 42px;
    letter-spacing: 2px;
    color: var(--ink);
  }
  .title-rule {
    position: absolute;
    top: 222px;
    left: 245px;
    width: 456px;
    height: 30px;
  }
  .title-rule .of {
    position: absolute;
    left: 0;
    right: 0;
    top: 0;
    text-align: center;
    font-family: "Parisienne", cursive;
    font-size: 20px;
    color: var(--ink-soft);
  }
  .ribbon {
    position: absolute;
    top: 262px;
    left: 205px;
    width: 536px;
    height: 76px;
  }
  .ribbon-label {
    position: absolute;
    top: 262px;
    left: 205px;
    width: 536px;
    height: 76px;
    line-height: 76px;
    text-align: center;
    font-family: "Arimo", sans-serif;
    font-size: 40px;
    letter-spacing: -0.5px;
    color: var(--white);
  }
  .presented {
    position: absolute;
    top: 372px;
    left: 0;
    right: 0;
    text-align: center;
    font-family: "Cabin", sans-serif;
    font-size: 29px;
    color: var(--ink-soft);
  }
  .recipient {
    position: absolute;
    top: 418px;
    left: 0;
    right: 0;
    text-align: center;
    margin: 0;
    font-family: "Montserrat", sans-serif;
    font-weight: 800;
    font-size: 66px;
    letter-spacing: 1px;
    color: var(--ink);
  }
  .citation {
    position: absolute;
    top: 526px;
    left: 170px;
    width: 606px;
    text-align: center;
    margin: 0;
    font-family: "Parisienne", cursive;
    font-size: 17px;
    line-height: 25px;
    color: #3b4d5c;
  }
  .seal {
    position: absolute;
    top: 650px;
    left: 378px;
    width: 190px;
    height: 190px;
  }
  .seal-name {
    position: absolute;
    top: 650px;
    left: 378px;
    width: 190px;
    height: 190px;
    display: flex;
    align-items: center;
    justify-content: center;
    text-align: center;
    font-family: "Lato", sans-serif;
    font-weight: 700;
    font-size: 19px;
    line-height: 23px;
    color: #1e3550;
  }
  .website {
    position: absolute;
    top: 852px;
    left: 0;
    right: 0;
    text-align: center;
    font-family: "Lato", sans-serif;
    font-size: 16px;
    color: var(--ink);
  }
  .art-cyclist,
  .art-rider {
    position: absolute;
    border-radius: 40px;
    background: radial-gradient(ellipse at center, var(--sketch), rgba(80, 130, 160, 0) 70%);
  }
  .art-cyclist { top: 890px; left: 140px; width: 290px; height: 250px; }
  .art-rider   { top: 790px; left: 520px; width: 400px; height: 370px; }
  .sign-line {
    position: absolute;
    top: 1090px;
    border-top: 2px dotted #3a4650;
    width: 210px;
    text-align: center;
    padding-top: 4px;
    font-family: "Lato", sans-serif;
    font-size: 15px;
    color: var(--ink);
  }
  .sign-date { left: 88px; }
  .sign-director { left: 700px; }
</style>
</head>
<body>
  <main class="certificate">
    <div class="sky-backdrop" role="img" aria-label="Soft sky and cloud backdrop in light blue"></div>

    <p class="org-name">CLEAR HARBOR<br>TRANSPORTATION MANAGEMENT ASSOCIATION</p>
    <div class="stars" aria-hidden="true">★★★</div>

    <h1 class="title">CERTIFICATE</h1>
    <div class="title-rule">
      <svg width="456" height="30" viewBox="0 0 456 30" aria-hidden="true">
        <path d="M0 16 L215 13" stroke="#1d2126" stroke-width="2.5" fill="none"/>
        <path d="M241 13 L456 16" stroke="#1d2126" stroke-width="2.5" fill="none"/>
      </svg>
      <span class="of">of</span>
    </div>

    <svg class="ribbon" viewBox="0 0 536 76" aria-hidden="true">
      <polygon points="0,0 536,0 508,38 536,76 0,76 28,38" fill="var(--ribbon)"/>
      <polygon points="0,0 28,38 0,76 44,76 44,0" fill="var(--ribbon-dark)" opacity="0.35"/>
    </svg>
    <div class="ribbon-label">APPRECIATION</div>

    <div class="presented">Presented to</div>
    <h2 class="recipient">Nora Whitfield</h2>

    <p class="citation">
      for her outstanding job of promoting commuting alternatives<br>
      (biking, walking, transit, ridesharing)<br>
      to driving alone, and as such have reduced<br>
      green house gas emissions.
    </p>

    <svg class="seal" viewBox="0 0 190 190" aria-hidden="true">
      <circle cx="95" cy="95" r="90" fill="var(--gold)"/>
    </svg>
    <div class="seal-name">Clear Harbor<br>TMA</div>

    <div class="website">www.clearharbortma.org</div>

    <div class="art-cyclist" role="img" aria-label="Faint line sketch of a commuter riding a bicycle"></div>
    <div class="art-rider" role="img" aria-label="Faint line sketch of a rider on horseback"></div>

    <div class="sign-line sign-date">Date</div>
    <div class="sign-line sign-director">Director</div>
  </main>
</body>
</html>
```